VORTAL Business Card Design

We need a business card for a new company based on the Gold Coast, we are a new supplement distributing company called VORTAL Sports Nutrition - Bold Horizon Sports Nutrition. We are providing new science based bodybuilding and fitness supplementation. Our company has a key focus towards next generation. We are wanting a card that is cool, innovative and fresh. We would like to see the implementation of the below image in a fresh and very innovative design that stands out. The final design should communicate New, Innovative, Cool, Science and researched based.
Target Market(s)
The target market is fitness and bodybuilder enthusiasts. Young audience so very cool looking.
Industry/Entity Type
Fitness
Contact Information for Business Card
(front of card)
VORTAL Sports Nutrition.
Liam Darrow
CEO/Sport Nutrition Specialist
0472 638 904
Liam@vortalsportsfuel.example
www.vortalsportsfuel.example
(back of card)
Scientifically formulated supplement range
Private Nutrition consultations
comprehensive sports nutrition seminars
Requirements
Nice to have
- The card could have a cut out on one of the sides or one of the corners rounded off so the card looks different from a normal business card.
Should not have
- The colours need to complement each other and pop out.

```html
<!DOCTYPE html>
<html lang="en">
<head>
<meta charset="utf-8">
<title>VORTAL Sports Nutrition – Business Card</title>
<link rel="stylesheet" href="https://fonts.googleapis.com/css2?family=Orbitron:wght@700;800&family=Michroma&display=swap">
<style>
  :root {
    --page: #ffffff;
    --card: #000000;
    --cyan: #3fe6ee;
    --cyan-soft: #8ff3f7;
    --white: #ffffff;
    --shadow: rgba(0, 0, 0, 0.55);
  }
  * { margin: 0; padding: 0; box-sizing: border-box; }
  html, body {
    width: 913px;
    height: 1200px;
    overflow: hidden;
    background: var(--page);
  }
  .sheet {
    position: relative;
    width: 913px;
    height: 1200px;
  }
  .card {
    position: absolute;
    left: 40px;
    width: 827px;
    height: 510px;
    background: var(--card);
    box-shadow: 0 0 14px 4px var(--shadow);
    color: var(--white);
    text-align: center;
  }
  .card--front { top: 40px; }
  .card--back { top: 638px; }

  .brand-mark {
    position: absolute;
    left: 321px;
    top: 41px;
    width: 186px;
    height: 186px;
  }
  .brand-mark__ring {
    position: absolute;
    inset: 0;
    border-radius: 50%;
    border: 4px solid var(--cyan-soft);
  }
  .brand-mark__name {
    position: absolute;
    left: 0;
    right: 0;
    top: 76px;
    font-family: "Orbitron", sans-serif;
    font-weight: 800;
    font-size: 28px;
    letter-spacing: 2px;
    color: var(--cyan);
  }

  .tagline {
    position: absolute;
    left: 0; right: 0;
    top: 236px;
    font-family: "Orbitron", sans-serif;
    font-weight: 800;
    font-size: 26px;
    letter-spacing: 0.5px;
    color: var(--cyan);
  }
  .contact { position: absolute; left: 0; right: 0; font-family: "Michroma", sans-serif; }
  .contact--name { top: 292px; font-size: 21px; color: var(--white); }
  .contact--role { top: 325px; font-size: 13px; color: var(--cyan); }
  .contact--phone { top: 353px; font-family: "Orbitron", sans-serif; font-weight: 700; font-size: 21px; letter-spacing: 1px; }
  .contact--email { top: 389px; font-size: 15px; }
  .contact--web {
    top: 465px;
    font-family: "Orbitron", sans-serif;
    font-weight: 700;
    font-size: 19px;
    color: var(--cyan);
    letter-spacing: 0.5px;
  }

  .rule {
    position: absolute;
    left: 75px;
    width: 677px;
    height: 2px;
    background: linear-gradient(90deg, transparent, var(--cyan) 50%, transparent);
  }
  .card--front .rule { top: 442px; }
  .card--back .rule--top { top: 321px; }
  .card--back .rule--bottom { top: 438px; }

  .services {
    position: absolute;
    left: 108px;
    top: 336px;
    list-style: none;
    text-align: left;
    font-family: "Michroma", sans-serif;
    font-size: 19px;
    color: var(--cyan);
  }
  .services__item {
    position: relative;
    padding-left: 48px;
    height: 29.5px;
    line-height: 29.5px;
  }
  .services__item::before {
    content: "";
    position: absolute;
    left: 0;
    top: 10px;
    width: 10px;
    height: 10px;
    border-radius: 50%;
    background: var(--cyan);
  }
</style>
</head>
<body>
<main class="sheet">
  <section class="card card--front" aria-label="Card front">
    <div class="brand-mark">
      <div class="brand-mark__ring"></div>
      <div class="brand-mark__name">VORTAL</div>
    </div>
    <h1 class="tagline">BOLD HORIZON SPORTS NUTRITION</h1>
    <p class="contact contact--name">LIAM DARROW</p>
    <p class="contact contact--role">CEO/Sport Nutrition Specialist</p>
    <p class="contact contact--phone">0472 638 904</p>
    <p class="contact contact--email">liam@vortalsportsfuel.example</p>
    <div class="rule"></div>
    <p class="contact contact--web">www.vortalsportsfuel.example</p>
  </section>

  <section class="card card--back" aria-label="Card back">
    <div class="brand-mark">
      <div class="brand-mark__ring"></div>
      <div class="brand-mark__name">VORTAL</div>
    </div>
    <div class="rule rule--top"></div>
    <ul class="services">
      <li class="services__item">Scientifically formulated supplement range</li>
      <li class="services__item">Private nutrition consultations</li>
      <li class="services__item">Comprehensive sports nutrition seminars</li>
    </ul>
    <div class="rule rule--bottom"></div>
  </section>
</main>
</body>
</html>
```